■概要 ・VKPへの出稿用バナー作成をしていただける方を募集します。 ---------------- ■注意点 ご提案頂きましたバナー案について、SNSへの投稿・Webサイトへのアップ等を行わないようにお願いします。 ※承諾頂ける方のみコンペへの参加をお願いします。 ---------------- ■依頼詳細 ・バナー内にテキストを挿入する場合は、テキストレイヤーで挿入してください。 ・テキストはおよそ1/4サイズで表示される事を考慮して制作して下さい。 ・配信時は制作したバナーがスマホの画面幅程度に縮小されて表示されます。テキストの可読性を考慮して制作お願いします ・バナー広告を見て、押したくなるようなバナー作成をお願いします。 【重要な指定】 ・脂肪吸引に注力したバナー。 ・参考URL https://www.kitahama-bodyline.example/index.html https://www.tsubaki-cl.example/ ・https://www.tsubaki-cl.example/のTOPページ上部の『10周年記念』のマークや『おかげさまで脂肪吸引総症例数15,000部位突破』などのフレーズ使用。 ・全体的に上品なイメージのバナー。 ・北浜美容ボディ案内所 ※このコンペは最大2件採用予定です。多数のバナーのご提案お待ちしております。 ■ 参考サイト(配信サイト) https://www.kitahama-bodyline.example/ ※対応方法の一部変更(9/27内容修正) ・コンペは今まで通り、1200×628 で行います。 ・採用になった作品の納品時に300×300のバナーを作成して頂き一緒に納品して頂きたいです ※300×300のバナーは採用バナーの簡易版としてつけて頂けると幸いです。 ⇒そのまま縮小というより、「メイン画像+社名(ロゴ)+一言キャッチ」くらい簡易的でOKです。 小さいバナーですので可読性を考慮して頂けると幸いです。 ■サイズと枚数 【コンペ】 ・1200 x 628 ・1枚 【納品時】 ・1200 x 628 → 1枚 ・300×300→ 1枚 ■納品ファイル ・フォトショップ形式(.psd) ■連絡事項 土日・祝日は対応することができません。 平日は9~18時までにご連絡いただければ、当日。 それ以降は翌日にご返信いたします。 ※VKPガイドラインに沿った内容である事 VKP掲載ガイドライン関連資料(https://help.zentravo.example/adrules/topic/4471829?hl=ja&ref_topic=5832014,7719203,) ※他で登録されているデザインや商標の転用など、他社の知的財産権を侵すこと ※他のクライアントへ既に提案した内容の転用など たくさんのウェブデザイナーの方からのご提案をお待ちしております。 |
どの案もよかったのですが、今回はこちらのバナーを特に気に入りました。
みなさんバナーの提案ありがとうございます。また依頼する際もどうぞよろしくお願いします。

```html
<!DOCTYPE html>
<html lang="ja">
<head>
<meta charset="utf-8">
<title>脂肪吸引バナー</title>
<link rel="stylesheet" href="https://fonts.googleapis.com/css2?family=Noto+Serif+JP:wght@500;600;700&family=Noto+Sans+JP:wght@500;700;900&display=swap">
<style>
  :root {
    --brown: #6e4b2c;
    --brown-dark: #4a3220;
    --ink: #2b2b2b;
    --pink-light: #fbe6f1;
    --pink: #f3b9d8;
    --band: #f1e7d3;
    --white: #ffffff;
    --photo-skin: #e9c9b6;
    --photo-denim: #3d5275;
    --photo-coat: #4d5566;
  }
  * { margin: 0; padding: 0; box-sizing: border-box; }
  html, body { width: 1200px; height: 628px; overflow: hidden; }
  body { font-family: "Noto Sans JP", sans-serif; color: var(--ink); }
  .banner {
    position: relative; width: 1200px; height: 628px; overflow: hidden;
    background: linear-gradient(100deg, #fff8fb 0%, var(--pink-light) 40%, var(--pink) 100%);
  }
  .model-photo {
    position: absolute; left: 0; top: 0; width: 400px; height: 564px;
    background: linear-gradient(180deg, var(--photo-skin) 0%, #e2bca6 48%, var(--photo-denim) 62%, #2f4263 100%);
    opacity: .9;
  }
  .site-label {
    position: absolute; left: 28px; top: 22px;
    font-family: "Noto Serif JP", serif; font-weight: 600; font-size: 22px; color: var(--brown-dark);
  }
  .brand {
    position: absolute; left: 28px; top: 50px;
    font-family: "Noto Serif JP", serif; font-weight: 600; font-size: 44px; letter-spacing: 6px; color: var(--brown-dark);
  }
  .headline {
    position: absolute; left: 408px; top: 112px;
    font-family: "Noto Serif JP", serif; font-weight: 600; font-size: 76px; line-height: 112px;
    color: var(--brown); letter-spacing: 2px;
  }
  .subcopy {
    position: absolute; left: 412px; top: 356px;
    font-weight: 700; font-size: 26px; color: var(--ink);
  }
  .qa-bubble {
    position: absolute; left: 842px; top: 52px; width: 210px; height: 140px;
  }
  .qa-bubble p {
    position: absolute; inset: 0; display: flex; flex-direction: column; justify-content: center; align-items: center;
    font-weight: 700; font-size: 24px; line-height: 32px; color: var(--ink); transform: rotate(8deg);
  }
  .doctor-photo {
    position: absolute; left: 930px; top: 196px; width: 270px; height: 368px;
    background: linear-gradient(180deg, rgba(233,201,182,0) 0%, #d9b39a 30%, var(--photo-coat) 55%, #3a4150 100%);
  }
  .doctor-name {
    position: absolute; left: 1122px; top: 214px; display: flex; gap: 6px; align-items: flex-start;
    writing-mode: vertical-rl; font-family: "Noto Serif JP", serif; font-weight: 700; color: var(--ink);
  }
  .doctor-name .role { font-size: 22px; }
  .doctor-name .name { font-size: 30px; letter-spacing: 4px; margin-top: 0; }
  .stats-band {
    position: absolute; left: 0; bottom: 0; width: 1200px; height: 64px; background: var(--band);
    display: flex; align-items: center; padding-left: 44px;
  }
  .stat-label {
    background: var(--white); border-radius: 20px; padding: 2px 22px;
    font-weight: 700; font-size: 24px; color: var(--brown-dark);
  }
  .stat-value {
    font-family: "Noto Serif JP", serif; font-weight: 600; font-size: 52px; line-height: 1; color: var(--brown);
    margin-left: 24px;
  }
  .stat-value small { font-size: 24px; margin-left: 2px; }
  .stat + .stat { margin-left: 72px; }
  .stat { display: flex; align-items: center; }
</style>
</head>
<body>
<div class="banner">
  <div class="model-photo" role="img" aria-label="ジーンズ姿の女性の引き締まったウエストの写真"></div>
  <p class="site-label">北浜美容ボディ案内所</p>
  <p class="brand">TSUBAKI</p>

  <h1 class="headline">脂肪吸引で、<br>美しい身体に。</h1>
  <p class="subcopy">技術と最新機器で安全な施術が可能です。</p>

  <div class="qa-bubble">
    <svg width="210" height="140" viewBox="0 0 210 140" aria-hidden="true">
      <ellipse cx="108" cy="66" rx="96" ry="58" fill="#ffffff"/>
      <path d="M40 100 L18 132 L66 112 Z" fill="#ffffff"/>
    </svg>
    <p><span>Q&amp;Aで</span><span>不安も解消</span></p>
  </div>

  <div class="doctor-photo" role="img" aria-label="腕を組んだ院長の写真"></div>
  <div class="doctor-name"><span class="role">院長</span><span class="name">森田 圭吾</span></div>

  <div class="stats-band">
    <div class="stat"><span class="stat-label">医療事故</span><span class="stat-value">0<small>件</small></span></div>
    <div class="stat"><span class="stat-label">年間症例数</span><span class="stat-value">1730<small>部位</small></span></div>
  </div>
</div>
</body>
</html>
```